RTV Engineering Business Card Design

We’re looking for an elegant, clean, and timeless business card design that communicates experience, capability, and reliability.

RTV Engineering was established in 1995 , we are a Government Contracting company providing Professional Services to the Department of Harbor Affairs, Frontier Resilience and the Signals Consortium. Our capabilities include: Acquisition & Program Management; Intelligence & Security Operations; Cyber, IT & Network Operations; Lifecycle Logistics & Asset Readiness; C5ISR Systems Engineering & Sustainment.

We want the card to reflect a straightforward, confident approach to business. The design should feel polished and professional without being flashy or overly corporate.

Design Direction
Clean, sophisticated, and uncluttered
Elegant but understated
Strong typography and thoughtful spacing
A timeless aesthetic rather than something overly trendy
Confident and established, with a sense of substance
Easy to read and practical in a real-world business setting

The overall impression should be: “These are experienced professionals who know what they’re doing, do what they say, and can be relied upon.”

We’re open to creative interpretations. The finished card should feel distinctive through its typography, proportions, layout, and attention to detail rather than through excessive graphics or visual effects.

We’re looking for a design that would make a potential client immediately feel that they’re dealing with a capable, trustworthy, and established company.

Company Colors: Navy and Gold/Yellow (but you do not need to use these colors on the card)
Company Name: RTV Engineering Associates, Inc. (known as RTV Engineering)
Website: rtvengineering-hq.example
Company Logo: Navy & Gold (other variations attached)

```html
<!DOCTYPE html>
<html lang="en">
<head>
<meta charset="utf-8">
<title>RTV Engineering – Business Card</title>
<link rel="stylesheet" href="https://fonts.googleapis.com/css2?family=Ubuntu:ital,wght@0,400;0,500;0,700;1,400&display=swap">
<style>
  :root {
    --navy: #0d123b;
    --gold: #fce34d;
    --paper: #ffffff;
    --backdrop: #e8e8e8;
  }
  * { margin: 0; padding: 0; box-sizing: border-box; }
  html, body { width: 1200px; height: 960px; overflow: hidden; }
  body {
    background: var(--backdrop);
    position: relative;
    font-family: "Ubuntu", sans-serif;
    color: var(--navy);
  }
  .card { position: absolute; overflow: hidden; }
  .card-band {
    position: absolute; left: 0; right: 0; bottom: 0;
    height: 19px; background: var(--gold);
  }
  .card-front { left: 155px; top: 48px; width: 749px; height: 428px; background: var(--paper); }
  .card-back { left: 295px; top: 507px; width: 750px; height: 429px; background: var(--navy); }

  .wordmark {
    position: absolute;
    font-family: "Ubuntu", sans-serif;
    font-weight: 700;
    line-height: 1;
    letter-spacing: -0.01em;
  }
  .card-front .wordmark { left: 79px; top: 192px; font-size: 88px; color: var(--navy); }
  .card-back .wordmark { left: 0; right: 0; top: 146px; text-align: center; font-size: 150px; color: var(--paper); }

  .divider {
    position: absolute; left: 356px; top: 96px;
    width: 2px; height: 259px; background: var(--navy);
  }

  .contact { position: absolute; left: 423px; top: 0; }
  .person-name {
    position: absolute; left: 0; top: 95px; white-space: nowrap;
    font-size: 29px; font-weight: 700;
  }
  .person-title {
    position: absolute; left: 0; top: 127px; white-space: nowrap;
    font-size: 18px; font-style: italic;
  }
  .detail {
    position: absolute; left: 35px; white-space: nowrap;
    font-size: 18px; line-height: 24px;
  }
  .icon { position: absolute; left: 0; fill: var(--navy); }
</style>
</head>
<body>

<section class="card card-front">
  <div class="wordmark">RTV</div>
  <div class="divider"></div>

  <div class="contact">
    <h1 class="person-name">Person Name</h1>
    <p class="person-title">Director</p>

    <svg class="icon" style="top:174px" width="18" height="26" viewBox="0 0 18 26" aria-hidden="true">
      <path d="M9 0a8.5 8.5 0 0 0-8.5 8.5C.5 15 9 26 9 26s8.5-11 8.5-17.5A8.5 8.5 0 0 0 9 0zm0 12a3.5 3.5 0 1 1 0-7 3.5 3.5 0 0 1 0 7z"/>
    </svg>
    <p class="detail" style="top:174px">4820 Harborline Avenue<br>Suite 310, Bayport Crest<br>VA 23999</p>

    <svg class="icon" style="top:266px" width="18" height="18" viewBox="0 0 24 24" aria-hidden="true">
      <path d="M6.6 10.8a15.2 15.2 0 0 0 6.6 6.6l2.2-2.2a1 1 0 0 1 1-.25 11.4 11.4 0 0 0 3.6.57 1 1 0 0 1 1 1V20a1 1 0 0 1-1 1A17 17 0 0 1 3 4a1 1 0 0 1 1-1h3.5a1 1 0 0 1 1 1c0 1.25.2 2.45.57 3.6a1 1 0 0 1-.25 1z"/>
      <path d="M14 2a8 8 0 0 1 8 8h-2a6 6 0 0 0-6-6zm0 4a4 4 0 0 1 4 4h-2a2 2 0 0 0-2-2z"/>
    </svg>
    <p class="detail" style="top:262px">555-014-2290</p>

    <svg class="icon" style="top:290px" width="19" height="18" viewBox="0 0 24 22" aria-hidden="true">
      <path d="M12 0 0 8v14h24V8zm0 3.2 8.4 5.6L12 14 3.6 8.8z"/>
    </svg>
    <p class="detail" style="top:286px">info@rtvengineering-hq.example</p>

    <svg class="icon" style="top:315px" width="18" height="18" viewBox="0 0 24 24" aria-hidden="true" fill="none" stroke="#0d123b" stroke-width="1.6">
      <circle cx="12" cy="12" r="10.5"/>
      <ellipse cx="12" cy="12" rx="4.5" ry="10.5"/>
      <path d="M1.5 12h21M3 6.5h18M3 17.5h18M12 1.5v21"/>
    </svg>
    <p class="detail" style="top:310px">www.rtvengineering-hq.example</p>
  </div>

  <div class="card-band"></div>
</section>

<section class="card card-back">
  <div class="wordmark">RTV</div>
  <div class="card-band"></div>
</section>

</body>
</html>
```